Flyer for customer acquisition.

Hello, We are a sportmanagement agency from Germany and we need information flyers for customer acquisition. It should be DinA4 and should have a modern but serious design. I have uploaded a information sheet, where you can find the text and the composition, the flyer should have. I also uploaded Pictures / Images, which you can use. Of course you can use other suitable images. If they are not free, I will buy them later. On the bottom of the flyer there has been the contact information. You will find them in the download section, too. If you have questions, just write me. If I forgot something, I will update the letter :) Thank you very much!
Ich brauche zusätzliche Tage um durchzusehen

```html
<!DOCTYPE html>
<html lang="de">
<head>
<meta charset="utf-8">
<title>NOVA-T Nachwuchsförderung Flyer</title>
<link href="https://fonts.googleapis.com/css2?family=Michroma&family=Open+Sans:wght@400;600;700&family=Open+Sans+Condensed:wght@700&display=swap" rel="stylesheet">
<style>
  :root {
    --stage: #e9e9ec;
    --hero-dark: #2a1a16;
    --hero-mid: #5a2a1c;
    --hero-fire: #c44a1a;
    --body-dark: #262626;
    --body-mid: #3a3a3a;
    --blue-bright: #1fb3ea;
    --blue-deep: #1b5db6;
    --blue-title: #1e9be0;
    --white: #ffffff;
    --muted: #d6d6d6;
  }
  * { box-sizing: border-box; margin: 0; padding: 0; }
  html, body { width: 1041px; height: 1200px; overflow: hidden; background: var(--stage); }
  .flyer {
    position: absolute; left: 94px; top: 0; width: 853px; height: 1200px; overflow: hidden;
    background: linear-gradient(180deg, var(--body-mid) 0%, var(--body-dark) 100%);
    font-family: "Open Sans", sans-serif; color: var(--white);
  }
  .hero {
    position: absolute; left: 0; top: 0; width: 853px; height: 600px;
    background: radial-gradient(ellipse at 25% 35%, var(--hero-fire) 0%, var(--hero-mid) 40%, var(--hero-dark) 85%);
  }
  .hero-photo {
    position: absolute; left: 33px; top: 22px; width: 340px; height: 445px;
    background: radial-gradient(ellipse at 50% 45%, #e4581c 0%, #a8361a 45%, rgba(60,25,18,0) 75%);
  }
  .hero-ball {
    position: absolute; left: 335px; top: 44px; width: 104px; height: 104px; border-radius: 50%;
    background: radial-gradient(circle at 40% 35%, #ffffff 0%, #cfcfcf 60%, #555 100%);
  }
  .brand {
    position: absolute; right: 42px; top: 60px; display: flex; align-items: center; gap: 12px;
    font-family: "Michroma", sans-serif; font-size: 30px; color: var(--white);
  }
  .brand-dot { width: 22px; height: 22px; border-radius: 50%; background: var(--white); }
  .title-block { position: absolute; right: 38px; top: 165px; text-align: right; font-family: "Michroma", sans-serif; }
  .title-main { font-size: 48px; line-height: 56px; font-weight: 400; }
  .title-sub { font-size: 22px; line-height: 32px; margin-top: 4px; }
  .title-sub-lg { font-size: 30px; line-height: 36px; }
  .tagline { color: var(--blue-title); font-size: 25px; line-height: 36px; margin-top: 14px; }
  .waves { position: absolute; left: 0; top: 380px; width: 853px; height: 230px; }
  .services { position: absolute; left: 0; top: 0; width: 853px; }
  .service { position: absolute; left: 0; width: 853px; }
  .service-label {
    position: absolute; left: 0; width: 320px; height: 54px; display: flex; align-items: center;
  }
  .service-icon {
    width: 61px; height: 54px; background: var(--blue-bright); display: flex; align-items: center; justify-content: center;
  }
  .service-bar {
    position: relative; height: 40px; flex: 1; display: flex; align-items: center; padding-left: 8px;
    background: var(--blue-deep); clip-path: polygon(0 0, 94% 0, 100% 100%, 0 100%);
    font-family: "Open Sans Condensed", "Open Sans", sans-serif; font-weight: 700; font-size: 14px; letter-spacing: .2px;
  }
  .service-bar.light { background: var(--blue-bright); color: #0f2a44; }
  .service-bar.light .label-text { color: var(--body-dark); }
  .service-bar::after {
    content: ""; position: absolute; right: 0; top: 0; width: 14px; height: 100%;
    background: var(--blue-bright); clip-path: polygon(0 0, 40% 0, 100% 100%, 60% 100%);
  }
  .service-text {
    position: absolute; left: 327px; width: 510px; font-size: 15.5px; line-height: 21.5px; color: var(--muted);
  }
  .deco { position: absolute; right: 0; bottom: 0; width: 300px; height: 170px; }
  .footnotes { position: absolute; left: 14px; top: 1090px; width: 560px; font-size: 9.5px; line-height: 13px; color: var(--muted); }
  .footnotes p + p { margin-top: 6px; }
  .contact { position: absolute; left: 14px; top: 1163px; display: flex; align-items: center; gap: 10px; font-size: 15.5px; }
  .contact-item { display: flex; align-items: center; gap: 6px; }
  .divider { width: 1px; height: 20px; background: #777; }
</style>
</head>
<body>
<main class="flyer">
  <section class="hero">
    <div class="hero-photo" role="img" aria-label="Jubelnder Fußballspieler im orangefarbenen Trikot vor Flammen"></div>
    <div class="hero-ball" role="img" aria-label="Fußball"></div>
    <div class="brand"><span class="brand-dot"></span><span>NOVA</span></div>
    <div class="title-block">
      <h1 class="title-main">NOVA-T</h1>
      <p class="title-sub">NACHWUCHSFÖRDERUNG</p>
      <p class="title-sub title-sub-lg">UND -MANAGEMENT</p>
      <p class="tagline">WIR BEGLEITEN DICH AUF<br>DEINEM WEG ZUM PROFI</p>
    </div>
    <svg class="waves" viewBox="0 0 853 230" aria-hidden="true">
      <path d="M0 70 C200 180 520 210 853 120 L853 150 C560 240 250 230 0 150 Z" fill="#1ea6e3"/>
      <path d="M20 25 C220 150 520 160 853 70 L853 100 C560 190 260 170 20 25 Z" fill="#1c7fd0"/>
      <path d="M420 100 C600 120 760 60 853 25 L853 60 C740 110 600 130 420 100 Z" fill="#2a6fd0"/>
    </svg>
  </section>

  <section class="services">
    <article class="service" style="top:603px">
      <div class="service-label" style="top:0"><div class="service-icon">
        <svg width="28" height="28" viewBox="0 0 28 28" fill="none" stroke="#fff" stroke-width="1.6"><path d="M3 25h22M6 25v-6M12 25v-10M18 25v-8M6 12l6-5 5 3 7-7"/></svg>
      </div><div class="service-bar"><span class="label-text">KARRIEREPLANUNG</span></div></div>
      <p class="service-text" style="top:-3px">Wir haben deine Karriere im Blick! In enger Absprache mit deinen Eltern und dir leiten wir die richtigen Maßnahmen und Schritte ein, um dein Ziel „Profifußballer“ zu realisieren.</p>
    </article>

    <article class="service" style="top:681px">
      <div class="service-label" style="top:0"><div class="service-icon">
        <svg width="28" height="28" viewBox="0 0 28 28" fill="none" stroke="#fff" stroke-width="1.6"><circle cx="14" cy="13" r="9"/><path d="M5 13h3v5H5zM20 13h3v5h-3zM20 20c-2 4-5 4-7 4"/></svg>
      </div><div class="service-bar light"><span class="label-text">STÄNDIGER ANSPRECHPARTNER</span></div></div>
      <p class="service-text" style="top:2px">Egal um welchen Themen es sich handelt, wir sind für dich da! Ein vertrauensvolles und freundschaftliches Verhältnis ist uns besonders wichtig.</p>
    </article>

    <article class="service" style="top:759px">
      <div class="service-label" style="top:0"><div class="service-icon">
        <svg width="28" height="28" viewBox="0 0 28 28" fill="none" stroke="#fff" stroke-width="1.6"><path d="M14 4v20M8 25h12M5 8h18M5 8l-3 8h6zM23 8l-3 8h6z"/></svg>
      </div><div class="service-bar"><span class="label-text">RECHTSBERATUNG / VERTRAGSRECHT</span></div></div>
      <p class="service-text" style="top:6px">Juristendeutsch und Kleingedrucktes? Kein Problem! Wir helfen dir den Durchblick zu behalten und holen immer das Beste für dich raus.</p>
    </article>

    <article class="service" style="top:846px">
      <div class="service-label" style="top:0"><div class="service-icon">
        <svg width="28" height="28" viewBox="0 0 28 28" fill="none" stroke="#fff" stroke-width="1.8"><circle cx="14" cy="14" r="11"/><path d="M14 9l4 3-1.5 5h-5L10 12z"/></svg>
      </div><div class="service-bar light"><span class="label-text">AUSRÜSTUNG</span></div></div>
      <p class="service-text" style="top:-6px">Wir besorgen dir deine Ausrüstung! Unsere Beziehungen zu den großen Sportartikelherstellern ermöglichen den Abschluss von Ausrüsterverträgen*.</p>
    </article>

    <article class="service" style="top:925px">
      <div class="service-label" style="top:0"><div class="service-icon">
        <svg width="28" height="28" viewBox="0 0 28 28" fill="none" stroke="#fff" stroke-width="1.6"><path d="M14 3l9 4v7c0 6-4 10-9 11-5-1-9-5-9-11V7z"/><path d="M14 10c2 3 3 4 3 6a3 3 0 0 1-6 0c0-2 1-3 3-6z"/></svg>
      </div><div class="service-bar"><span class="label-text">VORSORGE</span></div></div>
      <p class="service-text" style="top:2px">Verletzungen gehören leider zum Fußball dazu. Wir sichern dich ab, indem wir eine private Zusatzkrankenversicherung für dich abschließen.</p>
    </article>

    <article class="service" style="top:1009px">
      <div class="service-label" style="top:0"><div class="service-icon">
        <svg width="28" height="28" viewBox="0 0 28 28" fill="none" stroke="#fff" stroke-width="1.6"><circle cx="14" cy="14" r="3"/><circle cx="5" cy="5" r="2"/><circle cx="23" cy="5" r="2"/><circle cx="5" cy="23" r="2"/><circle cx="23" cy="23" r="2"/><path d="M7 7l5 5M21 7l-5 5M7 21l5-5M21 21l-5-5"/></svg>
      </div><div class="service-bar light"><span class="label-text" style="font-size:12.5px">KOOPERATIONSPARTNER NETZWERK</span></div></div>
      <p class="service-text" style="top:-15px">Kooperationspartner/Netzwerk Ob Entscheidungsträger oder Experte, wir kennen die richtigen Leute. Zusätzlich bieten wir dir eine große Bandbreite an Leistungen, die du jederzeit in Anspruch nehmen kannst*</p>
    </article>
  </section>

  <svg class="deco" viewBox="0 0 300 170" aria-hidden="true">
    <polygon points="0,170 80,80 180,170" fill="#1a4f7a"/>
    <polygon points="80,80 200,110 180,170" fill="#1e6aa0"/>
    <polygon points="200,110 280,0 300,40 300,170 180,170" fill="#2390c8"/>
    <polygon points="280,0 300,40 300,0" fill="#1a5d94"/>
  </svg>

  <footer>
    <div class="footnotes">
      <p>*Die Entscheidung über das Zustandekommen eines Ausrüstervertrags obliegt dem jeweiligen Sportartikelhersteller. Ist ein Abschluss aktuell nicht möglich, erhältst du von uns 2x pro Saison neue Fußballschuhe sowie weitere Ausrüstungsgegenstände.</p>
      <p>**Personal Training, Athletik-Training, Ernährungsberatung, Sportpsychologische Betreuung, uvm.</p>
    </div>
    <div class="contact">
      <span class="contact-item"><svg width="14" height="12" viewBox="0 0 14 12"><rect width="14" height="12" rx="1" fill="#1fb3ea"/><path d="M0 1l7 5 7-5" stroke="#262626" fill="none"/></svg>01234/5678900</span>
      <span class="divider"></span>
      <span class="contact-item"><svg width="14" height="14" viewBox="0 0 14 14"><path d="M3 1l3 3-2 2c1 2 2 3 4 4l2-2 3 3-2 2C6 13 1 8 1 3z" fill="#1fb3ea"/></svg>info@nova-t.example</span>
      <span class="divider"></span>
      <span class="contact-item"><svg width="14" height="14" viewBox="0 0 14 14" fill="none" stroke="#1fb3ea"><circle cx="7" cy="7" r="6"/><path d="M1 7h12M7 1c3 3 3 9 0 12M7 1c-3 3-3 9 0 12"/></svg>www.nova-t.example</span>
    </div>
  </footer>
</main>
</body>
</html>
```